Business Card Design for an Investment Company

We need a business card design for our private investment company, called Ashbourne Partners. Ashbourne Partners is an investments partnership that aims to acquire shares in listed companies with a view to influencing those companies through active dialogue in order to improve their value. We need designs that use the logo colors (blue, grey, white), we need both English and Arabic on the business cards (can be on one side or 2 sides). The final logo should communicate professionalism, conservatism (nothing too fancy or too cheesy), that we are smart, conservative and old school.

Target Market(s)

Investment companies

Industry/Entity Type

Investment

Contact Information for Business Card

Khalid Yousef Rumaithi
Senior Executive Officer

Palm Terrace 07, Level 3, Office 215/12
HLMZ

+9714987650
krumaithi@ashbournepartners.com
www.ashbournepartners.com

Requirements
Must have
• Logo to be placed on the left hand side of the business card
• for the Arabic, we only need to have the name and title so it can be accomodated on one side so we can have the other side with full color and logo. The arabic that needs to be used is the below:
• خالد يوسف الرميثي
• المدير التنفيدي

```html
<!DOCTYPE html>
<html lang="en">
<head>
<meta charset="utf-8">
<title>Ashbourne Partners — Business Card</title>
<link rel="stylesheet" href="https://fonts.googleapis.com/css2?family=Open+Sans:wght@400;700&family=Noto+Sans+Arabic:wght@400&display=swap">
<style>
  :root {
    --brand-blue: #1a6ea5;
    --text-blue: #1f63a0;
    --text-grey: #555a5e;
    --card-white: #ffffff;
    --backdrop: #e9e7e4;
  }
  * { box-sizing: border-box; margin: 0; padding: 0; }
  html, body { width: 1200px; height: 1000px; overflow: hidden; }
  body {
    position: relative;
    background: var(--backdrop);
    font-family: "Open Sans", Arial, sans-serif;
  }
  .card {
    position: absolute;
    left: 266px;
    width: 666px;
    height: 397px;
    box-shadow: 0 2px 8px rgba(0,0,0,0.12);
  }
  .card--front { top: 74px; background: var(--card-white); }
  .card--back { top: 534px; background: var(--brand-blue); display: flex; align-items: center; justify-content: center; }

  .wordmark { font-family: "Open Sans", Arial, sans-serif; font-weight: 700; letter-spacing: -0.5px; white-space: nowrap; }
  .card--front .wordmark {
    position: absolute; left: 32px; top: 176px;
    font-size: 27px; color: var(--brand-blue);
  }
  .card--back .wordmark { font-size: 46px; color: var(--card-white); }

  .details {
    position: absolute; left: 340px; top: 78px;
    font-size: 15.5px; line-height: 22px; color: var(--text-grey);
  }
  .details p { white-space: nowrap; }
  .person-name { color: var(--text-blue); font-size: 16.5px; }
  .arabic { font-family: "Noto Sans Arabic", Arial, sans-serif; font-size: 15px; line-height: 25px; }
  .arabic--name { color: var(--text-blue); }
  .address { margin-top: 26px; }
  .contact { margin-top: 9px; line-height: 24px; }
  .label { color: var(--text-blue); }
</style>
</head>
<body>
  <section class="card card--front">
    <div class="wordmark">Ashbourne Partners</div>
    <div class="details">
      <p class="person-name">Khalid Yousef Rumaithi</p>
      <p class="person-title">Senior Executive Officer</p>
      <p class="arabic arabic--name" dir="rtl" style="text-align:left">خالد يوسف الرميثي</p>
      <p class="arabic arabic--title" dir="rtl" style="text-align:left">المدير التنفيدي</p>
      <div class="address">
        <p>Palm Terrace 07, Level 3, Office</p>
        <p>215/12&nbsp; HLMZ</p>
      </div>
      <div class="contact">
        <p><span class="label">Phone:</span> +9714987650</p>
        <p><span class="label">Email:</span> krumaithi@ashbournepartners.com</p>
        <p><span class="label">Website:</span> www.ashbournepartners.com</p>
      </div>
    </div>
  </section>
  <section class="card card--back">
    <div class="wordmark">Ashbourne Partners</div>
  </section>
</body>
</html>
```